National Female Non-profit Business Card

We need a business card design as soon as possible for a non-profit organisation called Meadow to Summit. Our aim is to empower leadership potential in rural female teens.
The business card should have our logo on the one side and then information on the other side, including name, job title, email address, phone number and website (www.meadowtosummit.com.au) and our twitter handle @MeadowSummit
It should use the colours white, coral (#f04a50) and orange (#f68e4e). The font used in the logo is Raleway.
The hashtag #YoungVoicesRise could be used.
It should be bright, chic and crisp. Our logo is attached.

Target Market(s)
We will be handing the cards out to politicians and senior executives. However, as we're a non-profit for young women, they also need to reflect femininity and youth.
Industry/Entity Type
Non-Profit
Look and feel

```html
<!DOCTYPE html>
<html lang="en">
<head>
<meta charset="utf-8">
<title>Meadow to Summit — Business Card</title>
<link rel="stylesheet" href="https://fonts.googleapis.com/css2?family=Lato:wght@400;700;900&display=swap">
<style>
  :root {
    --backdrop: #3a3a3c;
    --card-dark: #1d1d1f;
    --card-dark-edge: #262628;
    --coral: #f04a50;
    --coral-deep: #d63a3f;
    --white: #ffffff;
    --cream: #f2ead0;
    --ink: #141414;
  }
  * { box-sizing: border-box; margin: 0; padding: 0; }
  html, body {
    width: 1200px; height: 926px; overflow: hidden;
    background: var(--backdrop);
  }
  .canvas {
    position: relative; width: 1200px; height: 926px;
    display: flex; flex-direction: column; align-items: center;
    justify-content: center; gap: 26px;
  }
  .card {
    position: relative; width: 700px; height: 400px; overflow: hidden;
    box-shadow: 0 10px 30px rgba(0,0,0,.35);
  }

  /* Name side */
  .card--brand { background: radial-gradient(circle at 50% 45%, var(--card-dark-edge), var(--card-dark) 75%); }
  .tab { position: absolute; width: 16px; height: 120px; background: var(--coral); border-radius: 3px; }
  .tab--left { left: 18px; top: 24px; }
  .tab--right { right: 18px; bottom: 24px; }
  .brand {
    position: absolute; left: 0; right: 0; top: 50%; transform: translateY(-50%);
    display: flex; align-items: center; justify-content: center; gap: 14px;
  }
  .brand__mark { width: 18px; height: 18px; background: var(--coral); flex: none; }
  .brand__name {
    font-family: "Lato", sans-serif; font-weight: 700; color: var(--white);
    font-size: 34px; letter-spacing: .5px;
  }

  /* Information side */
  .card--info { display: flex; }
  .info__side {
    width: 280px; height: 100%; position: relative;
    background: radial-gradient(circle at 50% 40%, var(--card-dark-edge), var(--card-dark) 80%);
  }
  .info__side .brand { top: 38%; gap: 8px; }
  .info__side .brand__name { font-size: 21px; }
  .info__side .brand__mark { width: 11px; height: 11px; }
  .handle {
    position: absolute; left: 0; right: 0; bottom: 62px;
    display: flex; flex-direction: column; align-items: center; gap: 10px;
  }
  .handle__dot { width: 20px; height: 20px; border-radius: 50%; background: var(--cream); }
  .handle__text { font-family: "Lato", sans-serif; font-weight: 700; color: var(--white); font-size: 19px; letter-spacing: .5px; }

  .info__main {
    flex: 1; padding: 52px 0 0 40px; color: var(--white);
    background: linear-gradient(160deg, var(--coral) 0%, var(--coral-deep) 70%, #b93036 100%);
  }
  .person { font-family: "Lato", sans-serif; color: var(--ink); font-size: 34px; line-height: 1; }
  .person__first { font-weight: 400; }
  .person__last { font-weight: 900; }
  .person__title { font-family: "Lato", sans-serif; color: var(--ink); font-size: 18px; margin-top: 6px; }
  .contacts { list-style: none; margin-top: 28px; display: flex; flex-direction: column; gap: 8px; }
  .contact {
    display: flex; align-items: flex-start; gap: 8px;
    font-family: "Lato", sans-serif; font-size: 20px; line-height: 1.3;
  }
  .contact__icon { width: 22px; height: 22px; flex: none; margin-top: 3px; }
</style>
</head>
<body>
<main class="canvas">

  <section class="card card--brand" aria-label="Card name side">
    <span class="tab tab--left"></span>
    <span class="tab tab--right"></span>
    <div class="brand">
      <span class="brand__mark"></span>
      <span class="brand__name">Meadow to Summit</span>
    </div>
  </section>

  <section class="card card--info" aria-label="Card information side">
    <div class="info__side">
      <div class="brand">
        <span class="brand__mark"></span>
        <span class="brand__name">Meadow to Summit</span>
      </div>
      <div class="handle">
        <span class="handle__dot"></span>
        <span class="handle__text">@MeadowSummit</span>
      </div>
    </div>

    <div class="info__main">
      <h1 class="person"><span class="person__first">Ellie </span><span class="person__last">Marsh</span></h1>
      <p class="person__title">Title goes here</p>

      <ul class="contacts">
        <li class="contact">
          <svg class="contact__icon" viewBox="0 0 22 22"><circle cx="11" cy="11" r="11" fill="#fff"/><path d="M7 6c1 0 1.6 1.8 1.6 2.4 0 .8-.9 1-.6 1.7.6 1.3 1.6 2.3 2.9 2.9.7.3.9-.6 1.7-.6.6 0 2.4.6 2.4 1.6 0 1-1.2 2-2.3 2C9.4 16 6 12.6 6 9.3 6 7.2 6 6 7 6z" fill="var(--coral)"/></svg>
          <span>123-555-0148</span>
        </li>
        <li class="contact">
          <svg class="contact__icon" viewBox="0 0 22 22"><circle cx="11" cy="11" r="11" fill="#fff"/><rect x="5.5" y="7" width="11" height="8" rx="1" fill="var(--coral)"/><path d="M5.8 7.5 11 11.5l5.2-4" stroke="#fff" stroke-width="1.2" fill="none"/></svg>
          <span>yourdomain.com</span>
        </li>
        <li class="contact">
          <svg class="contact__icon" viewBox="0 0 22 22"><circle cx="11" cy="11" r="11" fill="#fff"/><g stroke="var(--coral)" stroke-width="2" fill="none" stroke-linecap="round"><path d="M9.5 12.5 12.5 9.5"/><path d="M10.5 7.5l1-1a2.5 2.5 0 0 1 3.5 3.5l-1 1"/><path d="M11.5 14.5l-1 1a2.5 2.5 0 0 1-3.5-3.5l1-1"/></g></svg>
          <span>yourname@yourdomain.com</span>
        </li>
        <li class="contact">
          <svg class="contact__icon" viewBox="0 0 22 22"><circle cx="11" cy="11" r="11" fill="#fff"/><path d="M11 5.5 5 10.5h1.8V16h3v-3.2h2.4V16h3v-5.5H17z" fill="var(--coral)"/></svg>
          <span>Street address goes here,<br>Suite #410, Elm Bldg, NY 82417</span>
        </li>
      </ul>
    </div>
  </section>

</main>
</body>
</html>
```